Single Page Timetracking Dashboard Desktop App UI Design (Figma Link required)

Main Idea: a SaaS tool where employees can add their time and project in a playful way. There is a infographics and a list with tasks as well.

Based on the attached concept.png the brief is following:

- check the attached rough scribble
- add own ideas or change things if they add value
- Style: colourful, nerdy, professional saas, modern, beautiful, white space
- Quality expectation: inspiration1+2.png
- I will need a Figma link
- desktop only
- make something fresh and unique

Process:
I need to include 2-3 feedback rounds that will span probably around 7 days

Target Market(s)

Internal Business Tool for a Software Development Company

Industry/Entity Type

IT

Other font styles liked:
• Could be monospace, not a must though

Requirements
Must have
• At least one page; Figma Link to the design;
Nice to have
• Microinterations like drop-down, hover/active colors; functionality specifications
Should not have
• Mobile view

```html
<!DOCTYPE html>
<html lang="en">
<head>
<meta charset="utf-8">
<title>Time Tracking Dashboard</title>
<link rel="stylesheet" href="https://fonts.googleapis.com/css2?family=Nunito+Sans:wght@400;600;700;800&display=swap">
<style>
:root{
  --bg:#f5f5f5;
  --white:#ffffff;
  --ink:#1b1d22;
  --muted:#8d939c;
  --line:#e6e9ee;
  --blue:#1f73e8;
  --blue-sky:#4cc8f7;
  --blue-deep:#179bd3;
  --blue-tile:#2a9ed3;
  --blue-soft:#eef3fd;
  --orange:#f3a94f;
  --orange-light:#f6cc88;
  --green:#1aa339;
  --tag-green-bg:#e3f5e6;
  --tag-yellow-bg:#fdf3cf;
  --tag-yellow:#e0b12b;
  --tag-blue-bg:#dfe9fc;
  --tag-purple-bg:#efe2fb;
  --tag-purple:#b37ee5;
}
*{box-sizing:border-box;margin:0;padding:0}
html,body{width:1200px;height:1200px;overflow:hidden}
body{background:var(--bg);font-family:"Nunito Sans",sans-serif;color:var(--ink);display:flex}

/* sidebar */
.sidebar{width:86px;height:1200px;background:var(--white);display:flex;flex-direction:column;align-items:center;padding-top:20px;gap:22px;box-shadow:2px 0 12px rgba(0,0,0,.03)}
.app-name{display:flex;align-items:center;gap:4px;font-size:11px;font-weight:700;color:var(--blue);height:22px}
.app-name i{width:8px;height:8px;border-radius:50%;background:var(--blue)}
.nav-item{display:flex;flex-direction:column;align-items:center;gap:6px;font-size:11px;color:var(--muted)}
.nav-icon{width:40px;height:40px;border-radius:10px;background:var(--blue-soft);display:flex;align-items:center;justify-content:center}
.nav-item.active .nav-icon{background:var(--blue);box-shadow:0 6px 14px rgba(31,115,232,.35)}
.nav-item.active{color:var(--ink)}

.main{flex:1;padding:22px 26px;display:flex;flex-direction:column;gap:16px}

/* track panel */
.track{background:linear-gradient(120deg,var(--blue-sky),var(--blue-deep));border-radius:12px;padding:16px 18px 16px;color:var(--white)}
.track h1{font-size:24px;font-weight:800;margin-bottom:12px}
.track-body{display:flex;gap:14px}
.picker{background:var(--white);border-radius:8px;display:flex;color:var(--ink);flex:1;padding:12px}
.calendar{width:210px;border-right:1px solid var(--line);padding-right:12px}
.cal-head{display:flex;justify-content:space-between;align-items:center;font-size:12px;font-weight:700;margin-bottom:6px}
.cal-head span{color:var(--muted);font-size:10px}
.cal-grid{display:grid;grid-template-columns:repeat(7,1fr);row-gap:3px;text-align:center;font-size:10px}
.cal-grid .dow{color:var(--muted);font-size:8px}
.cal-grid .out{color:var(--muted)}
.cal-grid .sel span{display:inline-block;width:18px;height:18px;line-height:18px;border-radius:50%;background:var(--blue);color:var(--white)}
.selects{flex:1;padding-left:12px;display:flex;flex-direction:column;gap:8px}
.select{border:1px solid var(--line);border-radius:6px;padding:7px 10px;font-size:11px;display:flex;justify-content:space-between}
.links{list-style:none;font-size:10px;display:flex;flex-direction:column;gap:4px}
.links a{color:var(--blue)}
.durations{width:340px;background:var(--blue-tile);border-radius:8px;padding:12px;display:flex;flex-direction:column;gap:8px}
.chip-grid{display:grid;grid-template-columns:repeat(4,1fr);gap:7px}
.chip{background:var(--white);color:var(--ink);border-radius:7px;text-align:center;font-size:12px;font-weight:600;padding:6px 0}
.chip.on{background:linear-gradient(180deg,#3a8ff0,var(--blue));color:var(--white)}
.and{display:flex;align-items:center;gap:6px;font-size:8px}
.and::before,.and::after{content:"";flex:1;height:1px;background:rgba(255,255,255,.7)}
.and span{background:var(--white);color:var(--ink);border-radius:6px;padding:0 5px}
.save{align-self:flex-end;background:linear-gradient(180deg,#3a8ff0,var(--blue));border-radius:7px;font-size:12px;font-weight:700;padding:6px 20px;margin-top:2px}
.track-foot{display:flex;gap:12px;margin-top:12px}
.note{flex:1;background:var(--white);border-radius:8px;color:var(--muted);font-size:11px;padding:12px;height:54px}
.total-time{width:200px;background:#f2f4f7;border-radius:8px;color:var(--ink);font-weight:800;font-size:15px;padding:16px}

/* statistics */
.stats{background:linear-gradient(120deg,var(--orange-light),var(--orange));border-radius:12px;padding:12px 18px 16px}
.stats-head{display:flex;justify-content:space-between;align-items:center;color:var(--white);font-size:11px;margin-bottom:10px}
.dropdown{background:var(--white);color:var(--ink);border-radius:6px;padding:5px 10px;font-size:11px;display:flex;gap:14px;align-items:center}
.stat-cards{display:flex;gap:14px}
.stat-card{flex:1;background:var(--white);border-radius:8px;padding:12px 16px;display:flex;flex-direction:column}
.stat-top{display:flex;justify-content:space-between;align-items:center;font-size:11px;font-weight:600}
.stat-top .pill{border:1px solid var(--line);border-radius:6px;padding:4px 10px;font-size:10px}
.stat-body{display:flex;align-items:center;gap:28px;margin-top:6px}
.legend{list-style:none;font-size:11px;display:flex;flex-direction:column;gap:6px}
.legend li{display:flex;gap:6px}
.legend i{width:6px;height:6px;border-radius:1px;margin-top:5px}
.legend small{display:block;color:var(--muted);font-size:9px}

/* tasks */
.tasks{flex:1;background:var(--white);border-radius:12px;overflow:hidden;border-left:6px solid var(--blue-sky)}
.tasks-head{background:linear-gradient(120deg,var(--blue-sky),var(--blue-deep));color:var(--white);display:flex;justify-content:space-between;align-items:center;padding:10px 18px}
.tasks-head h2{font-size:18px;font-weight:700}
.tasks-list{padding:6px 18px}
.day{display:flex;justify-content:space-between;align-items:baseline;font-size:13px;font-weight:600;margin:6px 0 4px}
.day small{font-size:10px}
.task{background:var(--blue-soft);border-radius:8px;padding:7px 12px;display:flex;justify-content:space-between;margin-bottom:5px}
.tag{display:inline-block;font-size:8px;padding:1px 6px;border-radius:3px;margin-bottom:2px}
.tag.coding{background:var(--tag-green-bg);color:var(--green)}
.tag.pm-yellow{background:var(--tag-yellow-bg);color:var(--tag-yellow)}
.tag.pm-blue{background:var(--tag-blue-bg);color:var(--blue)}
.tag.meeting{background:var(--tag-purple-bg);color:var(--tag-purple)}
.task h3{font-size:13px;font-weight:600}
.task p{font-size:9px;color:#4d535c}
.task-side{text-align:right;display:flex;flex-direction:column;align-items:flex-end;gap:1px}
.task-side .icons{display:flex;gap:6px}
.task-side strong{font-size:13px}
.task-side small{font-size:9px;color:var(--muted)}
</style>
</head>
<body>
<nav class="sidebar">
  <div class="app-name"><i></i>Tally</div>
  <div class="nav-item active"><div class="nav-icon"><svg width="16" height="16" viewBox="0 0 24 24" fill="none" stroke="#fff" stroke-width="2"><circle cx="12" cy="12" r="9"/><path d="M12 7v5l3 2"/></svg></div>Clock</div>
  <div class="nav-item"><div class="nav-icon"><svg width="16" height="16" viewBox="0 0 24 24" fill="none" stroke="#1f3f8f" stroke-width="2"><rect x="3" y="4" width="18" height="12" rx="2"/><path d="M12 16v4M8 20h8M8 12v-2M12 12V8M16 12v-3"/></svg></div>Statistics</div>
  <div class="nav-item"><div class="nav-icon"><svg width="16" height="16" viewBox="0 0 24 24" fill="none" stroke="#1f3f8f" stroke-width="2"><rect x="4" y="7" width="16" height="13" rx="2"/><path d="M9 7V4h6v3M4 12h16"/></svg></div>Task</div>
  <div class="nav-item"><div class="nav-icon"><svg width="16" height="16" viewBox="0 0 24 24" fill="none" stroke="#1f3f8f" stroke-width="2"><circle cx="12" cy="8" r="4"/><path d="M4 21c0-4 4-6 8-6s8 2 8 6"/></svg></div>User</div>
</nav>

<main class="main">
  <section class="track">
    <h1>Track your time</h1>
    <div class="track-body">
      <div class="picker">
        <div class="calendar">
          <div class="cal-head"><span>◀</span>October 2023<span>▶</span></div>
          <div class="cal-grid">
            <div class="dow">Mon</div><div class="dow">Tue</div><div class="dow">Wed</div><div class="dow">Thu</div><div class="dow">Fri</div><div class="dow">Sat</div><div class="dow">Sun</div>
            <div class="out">28</div><div class="out">29</div><div class="out">30</div><div class="out">31</div><div>1</div><div>2</div><div>3</div>
            <div>4</div><div>5</div><div>6</div><div>7</div><div>8</div><div>9</div><div>10</div>
            <div>11</div><div>12</div><div>13</div><div>14</div><div>15</div><div>16</div><div>17</div>
            <div>18</div><div>19</div><div class="sel"><span>20</span></div><div>21</div><div>22</div><div>23</div><div>24</div>
            <div>25</div><div>26</div><div>27</div><div>28</div><div>29</div><div>30</div><div>31</div>
            <div class="out">1</div><div class="out">2</div><div class="out">3</div><div class="out">4</div><div class="out">5</div><div class="out">6</div><div class="out">7</div>
          </div>
        </div>
        <div class="selects">
          <div class="select">Select Project <span>▾</span></div>
          <div class="select">Select Customer <span>▾</span></div>
          <ul class="links">
            <li><a>Customer 1 Project 1</a></li>
            <li><a>Customer 2 Project 2</a></li>
            <li><a>Customer 1 Project 2</a></li>
            <li><a>Customer with long name and pro...</a></li>
          </ul>
        </div>
      </div>
      <div class="durations">
        <div class="chip-grid">
          <div class="chip on">1h</div><div class="chip">2h</div><div class="chip">3h</div><div class="chip">4h</div>
          <div class="chip">5h</div><div class="chip">6h</div><div class="chip">7h</div><div class="chip">8h</div>
        </div>
        <div class="and"><span>And</span></div>
        <div class="chip-grid">
          <div class="chip">0m</div><div class="chip on">15m</div><div class="chip">30m</div><div class="chip">45m</div>
        </div>
        <div class="save">Save</div>
      </div>
    </div>
    <div class="track-foot">
      <div class="note">What did you do?</div>
      <div class="total-time">1h 15m</div>
    </div>
  </section>

  <section class="stats">
    <div class="stats-head">Statistics <div class="dropdown">This Month <span>▾</span></div></div>
    <div class="stat-cards">
      <article class="stat-card">
        <div class="stat-top">Current Month <span class="pill">Total: 50:45 h</span></div>
        <div class="stat-body">
          <svg width="130" height="130" viewBox="0 0 130 130">
            <circle cx="65" cy="65" r="44" fill="#f1f5fb"/>
            <g fill="none" stroke-width="5" transform="rotate(-150 65 65)">
              <circle cx="65" cy="65" r="54" stroke="#1f73e8" stroke-dasharray="100 239"/>
              <circle cx="65" cy="65" r="54" stroke="#f3a94f" stroke-dasharray="0 106 90 143"/>
              <circle cx="65" cy="65" r="54" stroke="#1aa339" stroke-dasharray="0 202 120 17"/>
            </g>
            <circle cx="65" cy="65" r="18" fill="#fff" role="img" aria-label="Small illustration of a person reading"/>
          </svg>
          <ul class="legend">
            <li><i style="background:var(--blue)"></i><div>40:45 h<small>Customer A (60%)</small></div></li>
            <li><i style="background:var(--orange)"></i><div>10:00 h<small>Customer B (20%)</small></div></li>
            <li><i style="background:var(--green)"></i><div>02:00 h<small>Customer C (20%)</small></div></li>
            <li><i style="background:var(--blue-sky)"></i><div>03:00 h<small>Customer D (20%)</small></div></li>
          </ul>
        </div>
      </article>
      <article class="stat-card">
        <div class="stat-top">September <span class="pill">Gasamt: 114:00 h</span></div>
        <div class="stat-body">
          <svg width="130" height="130" viewBox="0 0 130 130">
            <circle cx="65" cy="65" r="44" fill="#f1f5fb"/>
            <g fill="none" stroke-width="5" transform="rotate(-150 65 65)">
              <circle cx="65" cy="65" r="54" stroke="#1f73e8" stroke-dasharray="100 239"/>
              <circle cx="65" cy="65" r="54" stroke="#f3a94f" stroke-dasharray="0 106 90 143"/>
              <circle cx="65" cy="65" r="54" stroke="#1aa339" stroke-dasharray="0 202 120 17"/>
            </g>
            <circle cx="65" cy="65" r="18" fill="#fff" role="img" aria-label="Small illustration of a person reading"/>
          </svg>
          <ul class="legend">
            <li><i style="background:var(--blue)"></i><div>40:45 h<small>Customer A (60%)</small></div></li>
            <li><i style="background:var(--orange)"></i><div>10:00 h<small>Customer B (20%)</small></div></li>
            <li><i style="background:var(--green)"></i><div>02:00 h<small>Customer C (20%)</small></div></li>
            <li><i style="background:var(--blue-sky)"></i><div>03:00 h<small>Customer D (20%)</small></div></li>
          </ul>
        </div>
      </article>
    </div>
  </section>

  <section class="tasks">
    <div class="tasks-head"><h2>Your Tasks</h2><div class="dropdown">This Month <span>▾</span></div></div>
    <div class="tasks-list">
      <div class="day">Wednesday <small>7H 30M</small></div>
      <div class="task">
        <div><span class="tag coding">Coding</span><h3>Customer A Project 1</h3><p>It tracks your progress from first until now</p></div>
        <div class="task-side"><div class="icons"><svg width="12" height="12" viewBox="0 0 24 24" fill="none" stroke="#333" stroke-width="2"><path d="M4 20h4L19 9l-4-4L4 16z"/></svg><svg width="12" height="12" viewBox="0 0 24 24" fill="none" stroke="#333" stroke-width="2"><rect x="3" y="4" width="18" height="5"/><path d="M5 9v11h14V9M10 13h4"/></svg></div><strong>4h 30m</strong><small>December 9th</small></div>
      </div>
      <div class="day">Tuesday <small>7H 30M</small></div>
      <div class="task">
        <div><span class="tag pm-yellow">Project Management</span><h3>Customer B Project 1</h3><p>It tracks your progress from first until now</p></div>
        <div class="task-side"><div class="icons"><svg width="12" height="12" viewBox="0 0 24 24" fill="none" stroke="#333" stroke-width="2"><path d="M4 20h4L19 9l-4-4L4 16z"/></svg><svg width="12" height="12" viewBox="0 0 24 24" fill="none" stroke="#333" stroke-width="2"><rect x="3" y="4" width="18" height="5"/><path d="M5 9v11h14V9M10 13h4"/></svg></div><strong>3h</strong><small>December 9th</small></div>
      </div>
      <div class="task">
        <div><span class="tag pm-blue">Project Management</span><h3>Customer A Project 1</h3><p>It tracks your progress from first until now</p></div>
        <div class="task-side"><div class="icons"><svg width="12" height="12" viewBox="0 0 24 24" fill="none" stroke="#333" stroke-width="2"><path d="M4 20h4L19 9l-4-4L4 16z"/></svg><svg width="12" height="12" viewBox="0 0 24 24" fill="none" stroke="#333" stroke-width="2"><rect x="3" y="4" width="18" height="5"/><path d="M5 9v11h14V9M10 13h4"/></svg></div><strong>5h</strong><small>December 9th</small></div>
      </div>
      <div class="task">
        <div><span class="tag coding">Coding</span><h3>Customer A Project 1</h3><p>It tracks your progress from first until now</p></div>
        <div class="task-side"><div class="icons"><svg width="12" height="12" viewBox="0 0 24 24" fill="none" stroke="#333" stroke-width="2"><path d="M4 20h4L19 9l-4-4L4 16z"/></svg><svg width="12" height="12" viewBox="0 0 24 24" fill="none" stroke="#333" stroke-width="2"><rect x="3" y="4" width="18" height="5"/><path d="M5 9v11h14V9M10 13h4"/></svg></div><strong>4h 30m</strong><small>December 9th</small></div>
      </div>
      <div class="day">Monday</div>
      <div class="task">
        <div><span class="tag meeting">Meeting</span><h3>Customer B Project 1</h3><p>It tracks your progress from first until now</p></div>
      </div>
    </div>
  </section>
</main>
</body>
</html>
```